Outbound Reach company is looking for a web page design

Your projects should contain:

1. Header: Logo provided by us.
2. Top nav bar: offer, about us, experience, contact.
3. “Choose language” button.
4. Main section: panoramic picture (static, professional, modern).
5. Below section: 3 blocks (image+title+description), which represent our 3 main activities (titles):
• Market Research,
• Marketing Plans,
• Marketing Project.
6. ‘Contact us’ form – Message (text: “Write your message and give us details about your company and activities”), Email, SEND).
7. Page footer: (4 section: Contact, Social Media, Blog, Partners).
Updates

Hello!

I uploaded new file 'general_look', which is our idea how the page should generally look like.

BUT! it doesn't mean that your projects should look exactly like this project e.g.:
* titles Market Research, Marketing Plans, Marketing Project can be above these: Image 1,2,3.
* everything doesn't have to be in square and rectangle shape. You can try to manipulate with blocks and can add elipse elemnts or something similar.

We will appreciate your innovative ideas. Just wanted to give you general plan of the site and ilustrate all elements that we require.

Best Regards,
Teodor

IMPORTENT

Please remember that the main picture should be panoramic. Please do not close it in frame.

Target Market(s)

Small and middle sized companies, which would like to export their goods and services abroad and are interested in raising funds from Coastal Alliance to expand their activities. These are rather industrial companies with low level of innovativeness. Our mission is to build image of the client’s company and increase awareness of their products to improve their competitiveness and innovativeness.

Industry/Entity Type

It Company

Requirements
Must have
• 1. Create designs of main page and subpage.
2. Subpage: Logo, Header, language button, place for article, navigation menu on the right side - below it “contact us” button , footer on the bottom. (In this section we are looking mainly for the design of the header and navigation menu).
3. The whole design should be a series of horizontal blocks.
4. Your projects should be associated with features such as: Reliability, Security, Professionalism, Openness, Uniqueness.
5. The design should be simple, fresh, readable, easy to use and should create a feeling of high quality services.
6. Possibility to change the panoramic picture (separate layer in a graphic file).
7. All pictures and blocks should be static, no movements.
8. Style of the page should be compliant with the logo design, font: Swiss.
9. Designs that we like: http://www.brixomedia.pl/, http://www.zentrofalu.com/.
Should not have
• There shouldn’t be any distractions and not matching parts (whole design should be compact and easy to interpret and remember).

```html
<!DOCTYPE html>
<html lang="en">
<head>
<meta charset="utf-8">
<title>Outbound Reach — Home</title>
<link href="https://fonts.googleapis.com/css2?family=Ubuntu:wght@400;500;700&family=Roboto:wght@400;500;700&display=swap" rel="stylesheet">
<style>
:root{
  --brand:#1d5e8f;
  --brand-dark:#0f3f66;
  --brand-deep:#0b3356;
  --ink:#222;
  --body:#5a5a5a;
  --muted:#8a8a8a;
  --band:#e9e9e9;
  --band-light:#f4f4f4;
  --white:#fff;
  --page-edge:#c9c9c9;
}
*{box-sizing:border-box;margin:0;padding:0}
html,body{width:960px;height:1200px;overflow:hidden;background:var(--white)}
body{font-family:"Roboto",Arial,sans-serif;color:var(--body);position:relative}
.page{position:absolute;left:70px;top:0;width:820px;height:1200px}
.abs{position:absolute}

/* header */
.site-header{left:0;top:0;width:820px;height:71px;
  background:linear-gradient(90deg,#c4c4c4 0%,#f6f6f6 18%,#fff 50%,#f6f6f6 82%,#c4c4c4 100%);}
.brand{left:96px;top:22px;display:flex;align-items:center;gap:6px}
.brand-dot{width:24px;height:24px;border-radius:50%;background:var(--brand)}
.brand-name{font-family:"Ubuntu",sans-serif;font-size:22px;font-weight:500;color:var(--brand-deep);letter-spacing:-.3px}
.lang-select{left:586px;top:10px;width:114px;height:17px;border:1px solid #b5b5b5;border-radius:9px;background:#fff;
  font-size:8px;color:#777;line-height:15px;padding-left:11px}
.lang-select .chev{position:absolute;right:-1px;top:-1px;width:17px;height:17px;border-radius:50%;
  background:linear-gradient(#e8eef5,#b9c8d8);border:1px solid #8fa3b8}
.flag{left:706px;top:11px;width:19px;height:14px;background:#2a3d7a;border:1px solid #fff;box-shadow:0 0 0 1px #bbb}
.main-nav{left:383px;top:37px;display:flex;align-items:center;font-family:"Ubuntu",sans-serif;font-size:16px;color:#2b2b2b}
.main-nav a{text-decoration:none;color:inherit;margin-right:22px}
.main-nav a.current{background:linear-gradient(#3f86bd,#134a78);color:#fff;border-radius:11px;padding:2px 14px;margin-right:9px;
  box-shadow:inset 0 1px 0 rgba(255,255,255,.35)}

/* hero */
.hero{left:0;top:71px;width:820px;height:322px;
  background:linear-gradient(180deg,#3d6f80 0%,#6f9aa6 28%,#c7d4d6 42%,#2f4650 55%,#1b2a33 80%,#121d24 100%)}
.hero-dots{left:382px;top:296px;display:flex;gap:4px}
.hero-dots span{width:12px;height:12px;border-radius:50%;background:rgba(235,235,235,.85)}
.hero-dots span.on{background:#1d6aa8}

/* services */
.services{left:0;top:393px;width:820px;height:283px;
  background:linear-gradient(180deg,#e4e4e4 0%,#fbfbfb 12%,#fff 50%,#fbfbfb 88%,#d9d9d9 100%)}
.service{top:24px;width:197px}
.service h2{font-family:"Ubuntu",sans-serif;font-weight:700;font-size:17.5px;color:var(--brand);letter-spacing:.1px;white-space:nowrap}
.service .photo{margin-top:9px;width:197px;height:124px;box-shadow:0 2px 4px rgba(0,0,0,.25)}
.service p{margin-top:19px;font-size:8.2px;line-height:10px;color:#777;letter-spacing:.1px}

/* welcome */
.welcome{left:0;top:677px;width:820px;height:296px;
  background:linear-gradient(180deg,#cfcfcf 0%,#ededed 3%,#f3f3f3 50%,#ececec 95%,#bdbdbd 100%)}
.welcome h1{left:97px;top:27px;font-family:"Ubuntu",sans-serif;font-weight:400;font-size:20px;color:#111;display:flex;align-items:center;gap:5px}
.welcome h1 .dot{width:22px;height:22px;border-radius:50%;background:var(--brand);margin-left:3px}
.welcome h1 .name{color:var(--brand-deep);font-weight:500}
.welcome .figure{left:95px;top:70px;width:93px;height:96px;border:2px solid #bbb;background:linear-gradient(180deg,#f6f9fc,#cfe2f2)}
.welcome .intro{left:198px;top:72px;width:272px;font-size:8px;line-height:10.9px;color:#333}
.points{left:106px;top:180px;width:370px;list-style:none}
.points li{display:flex;gap:11px;font-size:8px;line-height:11px;color:#333;margin-bottom:10px}
.points svg{flex:none;margin-top:-1px}
.divider{left:503px;top:75px;height:176px;border-left:1px dashed #aaa}
.contact-title{left:536px;top:20px;font-family:"Ubuntu",sans-serif;font-size:19px;color:#333}
.contact-form{left:535px;top:52px;width:190px;height:207px;border-radius:4px;
  background:linear-gradient(180deg,#2f77ae 0%,#0f4f82 60%,#0c3e68 100%);
  box-shadow:0 10px 8px -6px rgba(0,0,0,.25)}
.contact-form .field{position:absolute;left:13px;width:164px;background:#fff;font-size:8px;color:#aaa;font-style:italic;padding:5px 9px}
.contact-form .email{top:13px;height:23px}
.contact-form .message{top:41px;height:104px;line-height:10px;padding-top:5px}
.contact-form .send{position:absolute;left:43px;top:163px;width:100px;height:26px;border-radius:13px;
  background:linear-gradient(#fff,#dcdcdc);border:1px solid #999;font-family:"Ubuntu",sans-serif;font-size:18px;color:#333;
  text-align:center;line-height:24px}

/* footer */
.site-footer{left:0;top:973px;width:820px;height:156px;background:#fff}
.foot-col{top:29px}
.foot-col h3{font-family:"Ubuntu",sans-serif;font-weight:700;font-size:10px;color:#333}
.foot-col ul{list-style:none;margin-top:12px}
.foot-col li{position:relative;padding-left:12px;font-size:7.8px;line-height:10px;color:#777;margin-bottom:6px}
.foot-col li::before{content:"";position:absolute;left:0;top:2px;width:5px;height:5px;background:#555;border-radius:1px}
.join{font-size:8px;color:#444;margin-top:18px}
.social{display:grid;grid-template-columns:16px 16px;gap:14px 13px;margin-top:14px}
.social span{width:16px;height:16px;border-radius:50%;background:#666}
.partners{display:grid;grid-template-columns:repeat(4,26px);gap:7px 12px;margin-top:14px}
.partners span{height:15px;border-radius:2px}

.bottom-bar{left:0;top:1129px;width:820px;height:71px;
  background:linear-gradient(90deg,#c2c2c2 0%,#eee 20%,#fafafa 50%,#eee 80%,#c2c2c2 100%)}
.bottom-nav{left:0;top:24px;width:820px;text-align:center;font-size:8px;font-weight:700;color:#555;letter-spacing:.3px}
.copyright{left:0;top:42px;width:820px;text-align:center;font-size:7.5px;color:#333}
</style>
</head>
<body>
<div class="page">

  <header class="site-header abs">
    <div class="brand abs"><span class="brand-dot"></span><span class="brand-name">Outbound Reach</span></div>
    <div class="lang-select abs">Choose language<span class="chev"></span></div>
    <div class="flag abs" role="img" aria-label="English language flag"></div>
    <nav class="main-nav abs">
      <a class="current" href="#">Offer</a>
      <a href="#">About Us</a>
      <a href="#">Experience</a>
      <a href="#">Contact Us</a>
    </nav>
  </header>

  <section class="hero abs" role="img" aria-label="Panoramic photo of a modern city skyline with glass towers under a stormy evening sky">
    <div class="hero-dots abs"><span class="on"></span><span></span><span></span><span></span></div>
  </section>

  <section class="services abs">
    <article class="service abs" style="left:97px">
      <h2>MARKET RESEARCH</h2>
      <div class="photo" role="img" aria-label="Photo of cranes above a bridge under construction" style="background:linear-gradient(180deg,#5c7ea4 0%,#8aa3bd 60%,#b9bdbf 78%,#5e5f55 100%)"></div>
      <p>Lorem ipsum dolor sit amet, consectetur adipisicing elit, sed do eiusmod tempor incididunt ut labore et dolore magna aliqua. Ut enim ad minim veniam, quis nostrud exercitation ullamco laboris nisi ut aliquip ex ea commodo consequat. Duis aute irure dolor in reprehenderit in voluptate</p>
    </article>
    <article class="service abs" style="left:312px">
      <h2>MARKETING PLANS</h2>
      <div class="photo" role="img" aria-label="Photo of a steel arch bridge seen from below against a blue sky" style="background:linear-gradient(160deg,#6f8fb8 0%,#c9cfcf 40%,#8f8a74 65%,#3f5a32 100%)"></div>
      <p>Lorem ipsum dolor sit amet, consectetur adipisicing elit, sed do eiusmod tempor incididunt ut labore et dolore magna aliqua. Ut enim ad minim veniam, quis nostrud exercitation ullamco laboris nisi ut aliquip ex ea commodo consequat. Duis aute irure dolor in reprehenderit in voluptate</p>
    </article>
    <article class="service abs" style="left:526px">
      <h2>MARKETING PROJECTS</h2>
      <div class="photo" role="img" aria-label="Photo of a city skyline with high-rise buildings under a blue sky" style="background:linear-gradient(180deg,#2d6fb8 0%,#8ab6dc 45%,#7f8c8f 70%,#4f5a55 100%)"></div>
      <p>Lorem ipsum dolor sit amet, consectetur adipisicing elit, sed do eiusmod tempor incididunt ut labore et dolore magna aliqua. Ut enim ad minim veniam, quis nostrud exercitation ullamco laboris nisi ut aliquip ex ea commodo consequat. Duis aute irure dolor in reprehenderit in voluptate</p>
    </article>
  </section>

  <section class="welcome abs">
    <h1 class="abs">Welcome to <span class="dot"></span><span class="name">Outbound Reach</span></h1>
    <div class="figure abs" role="img" aria-label="Illustration of business silhouettes standing on a rising blue bar chart"></div>
    <p class="intro abs">Lorem ipsum dolor sit amet, consectetur adipisicing elit, sed do eiusmod tempor incididunt ut labore et dolore magna aliqua. Ut enim ad minim veniam, quis nostrud exercitation ullamco laboris nisi ut aliquip ex ea commodo consequat. Duis aute irure dolor in reprehenderit in voluptate velit esse cillum dolore eu fugiat nulla pariatur. Excepteur sint occaecat cupidatat non proident, sunt in culpa qui officia deserunt mollit anim id est laborum.Lorem ipsum dolor sit amet, consectetur adipisicing elit, sed do eiusmod tempor incididunt ut labore et dolore magna aliqua. Ut enim ad minim veniam, quis nostrud exercitation ullamco laboris nisi ut aliquip.</p>
    <ul class="points abs">
      <li><svg width="18" height="18" viewBox="0 0 18 18"><circle cx="9" cy="9" r="9" fill="#1d5e8f"/><path d="M4.5 9h8M9 5l4 4-4 4" stroke="#fff" stroke-width="2" fill="none" stroke-linecap="round" stroke-linejoin="round"/></svg><span>Lorem ipsum dolor sit amet, consectetur adipisicing elit.ed do eiusmod tempor incididunt ut labore.</span></li>
      <li><svg width="18" height="18" viewBox="0 0 18 18"><circle cx="9" cy="9" r="9" fill="#1d5e8f"/><path d="M4.5 9h8M9 5l4 4-4 4" stroke="#fff" stroke-width="2" fill="none" stroke-linecap="round" stroke-linejoin="round"/></svg><span>Lorem ipsum dolor sit amet, consectetur adipisicing elit.ed do eiusmod tempor incididunt ut labore.</span></li>
      <li><svg width="18" height="18" viewBox="0 0 18 18"><circle cx="9" cy="9" r="9" fill="#1d5e8f"/><path d="M4.5 9h8M9 5l4 4-4 4" stroke="#fff" stroke-width="2" fill="none" stroke-linecap="round" stroke-linejoin="round"/></svg><span>Lorem ipsum dolor sit amet, consectetur adipisicing elit.ed do eiusmod tempor incididunt ut labore.</span></li>
    </ul>
    <div class="divider abs"></div>

    <h2 class="contact-title abs">Contact Us</h2>
    <form class="contact-form abs">
      <div class="field email">Email</div>
      <div class="field message">Write your message and give details about your company and activities.</div>
      <div class="send">Send</div>
    </form>
  </section>

  <footer class="site-footer abs">
    <div class="foot-col abs" style="left:92px">
      <h3>Contact Us</h3>
      <ul>
        <li>48 Harbor Row Millbrook<br>City 40215</li>
        <li>+1-555-014-2290</li>
        <li>hello@outboundreach.example</li>
      </ul>
    </div>
    <div class="foot-col abs" style="left:257px">
      <h3>Social Media</h3>
      <p class="join">Join us @</p>
      <div class="social"><span></span><span></span><span></span><span></span></div>
    </div>
    <div class="foot-col abs" style="left:389px">
      <h3>Blog</h3>
      <ul>
        <li>Lorem ipsum dolor sit amet<br>onsectetur adipisicing eli</li>
        <li>Lorem ipsum dolor sit amet<br>onsectetur adipisicing eli</li>
        <li>Lorem ipsum dolor sit amet<br>onsectetur adipisicing eli</li>
        <li>Lorem ipsum dolor sit amet<br>onsectetur adipisicing eli</li>
      </ul>
    </div>
    <div class="foot-col abs" style="left:573px">
      <h3>Partners</h3>
      <div class="partners">
        <span style="background:#c8322b"></span><span style="background:#8bb04a"></span><span style="background:#d23b35"></span><span style="background:#3f8f3a"></span>
        <span style="background:#222"></span><span style="background:#777"></span><span style="background:#2f4f8f"></span><span style="background:#222"></span>
        <span style="background:#999"></span><span style="background:#bbb"></span><span style="background:#3b7a3b"></span><span style="background:#aaa"></span>
        <span style="background:#c0392b"></span><span style="background:#6fbf3a"></span><span style="background:#e39a3b"></span><span style="background:#2c3e8c"></span>
      </div>
    </div>
  </footer>

  <div class="bottom-bar abs">
    <p class="bottom-nav abs">HOME | OFFER | ABOUT US | EXPERIENCE | CONTACT US</p>
    <p class="copyright abs">© 2012 Outbound Reach. All Rights Reserved.</p>
  </div>

</div>
</body>
</html>
```